New web page, 2 companies on the one page

A new web page for an engineering consultancy and maintenance management company

Corrick & Associates is the parent company covering the design and consultancy
Trivolt Engineering is the Maintenance and Reliability company

Target Market(s)

Food & Beverage, ingredients Manufacturing
engineering managers

Coding

Coded - Design and coding required

Number of Pages Required

1 page

Font styles to use
Other font styles liked:
• Roboto

Colors
1861ab
85acd3
d0dfed
cee9f5

```html
<!DOCTYPE html>
<html lang="en">
<head>
<meta charset="utf-8">
<title>Corrick &amp; Associates and Trivolt Engineering — Manufacturing Engineering Support</title>
<link href="https://fonts.googleapis.com/css2?family=Orbitron:wght@700;800;900&family=Montserrat:wght@400;500;600;700&family=Roboto:wght@400;500;700&display=swap" rel="stylesheet">
<style>
:root{
  --brand:#0aa2df;
  --brand-dark:#1861ab;
  --mid:#85acd3;
  --pale:#d0dfed;
  --sky:#cee9f5;
  --ink:#1b1b1b;
  --muted:#4a4a4a;
  --white:#ffffff;
  --black:#050505;
}
*{box-sizing:border-box;margin:0;padding:0}
html,body{width:1200px;height:5357px;overflow:hidden}
body{font-family:"Roboto",sans-serif;color:var(--ink);background:var(--white)}
.page{width:1200px;height:5357px;position:relative;overflow:hidden}
.display{font-family:"Orbitron",sans-serif;font-weight:900;text-transform:uppercase}
h2.section-title{font-family:"Orbitron",sans-serif;font-weight:900;font-size:32px;letter-spacing:1px;text-align:center;color:var(--ink)}
h2.section-title::after{content:"";display:block;width:60px;height:3px;background:var(--brand);margin:10px auto 0}

/* header */
.site-header{height:70px;display:flex;align-items:center;padding:0 82px 0 92px;justify-content:space-between}
.brand{display:flex;align-items:center;gap:10px;font-family:"Montserrat",sans-serif;font-weight:700;font-size:18px;color:var(--brand-dark);white-space:nowrap}
.brand-mark{width:34px;height:34px;border-radius:50%;background:var(--brand-dark);flex:none}
.nav{display:flex;align-items:center;gap:46px;font-family:"Montserrat",sans-serif;font-size:14px}
.nav a{color:var(--ink);text-decoration:none}
.nav a.active{border-bottom:2px solid var(--ink);padding-bottom:3px}
.btn{display:inline-block;background:var(--brand);color:var(--white);font-family:"Montserrat",sans-serif;font-size:13px;font-weight:600;padding:8px 28px;text-decoration:none;white-space:nowrap}
.btn-outline{background:var(--white);color:var(--brand)}

/* hero */
.hero{height:545px;position:relative;overflow:hidden}
.hero-photo{position:absolute;inset:0;background:linear-gradient(100deg,#2c3a4a 0%,#4c6f8c 45%,#9dbcd6 75%,#c9dbe8 100%)}
.hero-swoosh{position:absolute;right:0;bottom:0;width:1200px;height:545px}
.hero-copy{position:absolute;left:82px;top:205px;color:var(--white)}
.hero-copy h1{font-family:"Orbitron",sans-serif;font-weight:900;font-size:40px;letter-spacing:1px;line-height:1.15}
.hero-copy h1 span{display:block;font-size:28px;font-weight:800;letter-spacing:1px;line-height:1.5}
.hero-copy p{font-size:14px;line-height:1.4;margin:12px 0 20px;width:460px}
.hero-copy .btn{margin-right:22px;padding:7px 26px}

/* about */
.about-wrap{height:390px;background:var(--sky)}
.about{height:390px;background:var(--white);border-bottom-right-radius:260px 150px;display:flex;align-items:center;padding:0 0 0 105px;gap:110px}
.about-text{width:510px}
.about-text h2{font-family:"Orbitron",sans-serif;font-weight:900;font-size:32px;letter-spacing:1px;margin-bottom:26px;padding-left:10px}
.about-text p{font-size:12.5px;line-height:1.45;color:var(--muted);margin-bottom:22px}
.about-brand{width:290px;text-align:center;font-family:"Montserrat",sans-serif;font-weight:700;font-size:20px;color:var(--brand-dark)}
.about-brand .square{width:190px;height:190px;background:linear-gradient(135deg,var(--brand-dark),var(--mid));margin:0 auto 18px;border-radius:10px}

/* process */
.process{height:485px;background:var(--sky);padding-top:40px}
.process-cards{display:flex;justify-content:center;gap:72px;margin-top:70px}
.step-card{width:236px;height:290px;background:var(--white);border-radius:4px 4px 40px 4px;box-shadow:0 6px 12px rgba(0,0,0,.12);text-align:center;padding:30px 34px 0}
.step-card.active{background:var(--brand);color:var(--white)}
.step-icon{width:70px;height:70px;border-radius:50%;background:var(--brand);margin:0 auto 14px;display:flex;align-items:center;justify-content:center}
.step-card.active .step-icon{background:var(--white)}
.step-card h3{font-size:13px;font-weight:500;margin-bottom:10px}
.step-card p{font-size:11.5px;line-height:1.4}

/* services */
.services{height:2175px;background:var(--brand);padding-top:95px;color:var(--white)}
.services h2.section-title{color:var(--white)}
.services h2.section-title::after{background:var(--ink)}
.service-row{display:flex;align-items:center;height:336px;padding:0 150px 0 155px;justify-content:space-between}
.service-row:first-of-type{margin-top:75px}
.service-row.reverse{flex-direction:row-reverse;padding:0 170px 0 158px}
.service-photo{width:370px;height:300px;border-radius:16px 80px 16px 80px/16px 40px 16px 40px;flex:none}
.service-text{width:380px}
.service-text h3{font-family:"Montserrat",sans-serif;font-weight:500;font-size:26px;margin-bottom:12px;white-space:nowrap}
.service-text h3::after{content:"";display:block;width:80px;height:2px;background:var(--white);margin-top:8px}
.service-text p{font-size:12.5px;line-height:1.7;font-weight:400}

/* reviews */
.reviews{height:630px;padding-top:100px}
.review-cards{display:flex;justify-content:center;gap:40px;margin-top:60px}
.review-card{width:290px;height:330px;background:var(--brand);position:relative;box-shadow:0 4px 10px rgba(0,0,0,.1);color:var(--white);text-align:center}
.review-top{background:var(--white);color:var(--muted);height:200px;border-bottom-right-radius:90px 60px;padding:26px 36px 0;text-align:left}
.review-top .quote{font-family:"Montserrat",sans-serif;font-size:34px;font-weight:700;color:var(--brand);line-height:1}
.review-top p{font-size:10.5px;line-height:1.5;text-align:center}
.avatar{width:64px;height:64px;border-radius:50%;background:var(--pale);border:3px solid var(--white);position:absolute;left:113px;top:168px}
.review-name{position:absolute;top:245px;width:100%;font-size:11px;font-weight:700}
.review-social{position:absolute;top:272px;width:100%;display:flex;justify-content:center;gap:8px}
.review-social span,.footer-social span{width:11px;height:11px;border-radius:50%;background:var(--white)}

/* contact */
.contact{height:680px;padding-top:90px}
.contact-box{width:887px;height:500px;margin:0 0 0 153px;display:flex;box-shadow:0 4px 14px rgba(0,0,0,.12);position:relative;overflow:hidden}
.contact-photo{width:445px;height:100%;background:linear-gradient(120deg,#7b8a98,#d8dde2 60%,#eef0f2)}
.contact-form{padding:52px 40px 0 44px;flex:1}
.contact-form h2{font-family:"Orbitron",sans-serif;font-weight:900;font-size:26px;letter-spacing:1px;margin-bottom:26px}
.field{display:block;border:1.5px solid var(--brand);height:36px;margin-bottom:20px;padding:9px 12px;font-size:12px;color:var(--muted)}
.field.message{height:110px}
.contact-corner{position:absolute;right:0;bottom:0}

/* footer */
.site-footer{height:382px;position:relative;background:var(--black);color:var(--white)}
.footer-curve{position:absolute;left:0;top:-1px}
.footer-inner{position:absolute;top:150px;left:0;width:100%;display:flex;padding:0 0 0 105px}
.footer-about{width:290px}
.footer-brand{display:flex;align-items:center;gap:10px;font-family:"Montserrat",sans-serif;font-weight:700;font-size:19px;margin-bottom:26px;margin-top:20px;white-space:nowrap}
.footer-brand .brand-mark{width:44px;height:44px;background:var(--brand)}
.footer-about p{font-size:9.5px;line-height:1.5;color:#cfcfcf}
.footer-col h4{font-size:11px;font-weight:700;margin-bottom:14px}
.footer-col ul{list-style:none;font-size:10.5px;line-height:2}
.footer-col li::before{content:"";display:inline-block;width:6px;height:6px;border-radius:50%;background:var(--white);margin-right:10px;vertical-align:middle}
.col-quick{margin-left:94px;width:165px}
.col-services{width:310px}
.email-box{display:flex;align-items:center;justify-content:space-between;background:var(--white);color:var(--muted);font-size:10px;width:112px;height:20px;padding:0 6px}
.footer-social{display:flex;gap:8px;margin-top:12px;padding-left:12px}
.copyright{position:absolute;bottom:6px;width:100%;text-align:center;font-size:10px;color:#bdbdbd}
</style>
</head>
<body>
<div class="page">

<header class="site-header">
  <div class="brand"><span class="brand-mark"></span>Corrick &amp; Associates</div>
  <nav class="nav">
    <a class="active" href="#">Home</a><a href="#">About</a><a href="#">Process</a><a href="#">Services</a><a href="#">Reviews</a><a href="#">Contact</a>
    <a class="btn" href="#">Order now</a>
  </nav>
</header>

<section class="hero">
  <div class="hero-photo" role="img" aria-label="Two laboratory technicians in white coats and hairnets reviewing a tablet beside a food production line"></div>
  <svg class="hero-swoosh" viewBox="0 0 1200 545" aria-hidden="true">
    <path d="M0 545 L0 525 C300 535 900 535 1030 500 C1130 470 1185 420 1200 390 L1200 545 Z" fill="#0aa2df"/>
    <path d="M0 545 L0 538 C350 545 950 545 1080 515 C1150 495 1190 455 1200 440 L1200 545 Z" fill="#ffffff"/>
  </svg>
  <div class="hero-copy">
    <h1>MANUFACTURING<span>ENGINEERING SUPPORT</span><span>ORGANISATION</span></h1>
    <p>Lorem ipsum dolor sit amet, consectetur adipiscing elit. Scelerisque pellentesque sollicitudin diam vitae consectetur est sit.</p>
    <a class="btn" href="#">Learn more</a><a class="btn btn-outline" href="#">Learn More</a>
  </div>
</section>

<div class="about-wrap">
  <section class="about">
    <div class="about-text">
      <h2>ABOUT US</h2>
      <p>Corrick &amp; Associates is a specialised manufacturing engineering support organisation that can provide fast, nimble, and flexible design and consultancy services. Our sister company Trivolt Engineering delivers maintenance and reliability. Together we have a proven track record in process design and fit-out, project management and maintenance execution. Our focus on food manufacturing lets our team deliver real gains in performance and return on the client's investment.</p>
      <a class="btn" href="#">Learn more</a>
    </div>
    <div class="about-brand"><div class="square" role="img" aria-label="Company emblem area"></div>Trivolt Engineering</div>
  </section>
</div>

<section class="process">
  <h2 class="section-title">PROCESS</h2>
  <div class="process-cards">
    <div class="step-card">
      <div class="step-icon"><svg width="34" height="34" viewBox="0 0 24 24" fill="none" stroke="#fff" stroke-width="1.6"><path d="M3 12l4-4 4 3 3-3 7 5-5 5-3-2-3 2z"/></svg></div>
      <h3>STEP 01</h3>
      <p>Lorem ipsum dolor sit amet, consectetur adipiscing elit. Id natoque suspendisse donec quis urna, rhoncus risus sagittis pellentesque. Mauris velit diam et pulvinar.</p>
    </div>
    <div class="step-card active">
      <div class="step-icon"><svg width="34" height="34" viewBox="0 0 24 24" fill="none" stroke="#0aa2df" stroke-width="1.6"><circle cx="9" cy="9" r="4"/><circle cx="15" cy="15" r="4"/></svg></div>
      <h3>STEP 02</h3>
      <p>Lorem ipsum dolor sit amet, consectetur adipiscing elit. Id natoque suspendisse donec quis urna, rhoncus risus sagittis pellentesque. Mauris velit diam et pulvinar.</p>
    </div>
    <div class="step-card">
      <div class="step-icon"><svg width="34" height="34" viewBox="0 0 24 24" fill="none" stroke="#fff" stroke-width="1.6"><rect x="5" y="4" width="14" height="17" rx="2"/><path d="M9 11l2 2 4-4M9 17h6"/></svg></div>
      <h3>STEP 03</h3>
      <p>Lorem ipsum dolor sit amet, consectetur adipiscing elit. Id natoque suspendisse donec quis urna, rhoncus risus sagittis pellentesque. Mauris velit diam et pulvinar.</p>
    </div>
  </div>
</section>

<section class="services">
  <h2 class="section-title">OUR SERVICES</h2>
  <div class="service-row">
    <div class="service-photo" role="img" aria-label="Technician in protective clothing checking a clipboard at a control panel" style="background:linear-gradient(135deg,#c8d8e6,#5f7f9c)"></div>
    <div class="service-text"><h3>Major Equipment</h3><p>Lorem ipsum dolor sit amet, consectetur adipiscing elit. Nulla sed cum nunc, egestas placerat vulputate id vitae, a id pellentesque suspendisse tortor mi elementum interdum mauris venenatis lorem ipsum dolor sit amet, consectetur adipiscing elit. Nulla sed cum nunc, egestas placerat vulputate id vitae, a id pellentesq.</p></div>
  </div>
  <div class="service-row reverse">
    <div class="service-photo" role="img" aria-label="Engineers inspecting machinery in a workshop" style="background:linear-gradient(135deg,#e5e9ec,#7e8d98)"></div>
    <div class="service-text"><h3>Maintenance Management</h3><p>Lorem ipsum dolor sit amet, consectetur adipiscing elit. Nulla sed cum nunc, egestas placerat vulputate id vitae, a id pellentesque suspendisse tortor mi elementum interdum mauris venenatis lorem ipsum dolor sit amet, consectetur adipiscing elit. Nulla sed cum nunc, egestas placerat vulputate id vitae, a id pellentesq.</p></div>
  </div>
  <div class="service-row">
    <div class="service-photo" role="img" aria-label="Stainless steel processing plant with pipework and tanks" style="background:linear-gradient(135deg,#b6bcc2,#5b636b)"></div>
    <div class="service-text"><h3>Maintenance Execution</h3><p>Lorem ipsum dolor sit amet, consectetur adipiscing elit. Nulla sed cum nunc, egestas placerat vulputate id vitae, a id pellentesque suspendisse tortor mi elementum interdum mauris venenatis lorem ipsum dolor sit amet, consectetur adipiscing elit. Nulla sed cum nunc, egestas placerat vulputate id vitae, a id pellentesq.</p></div>
  </div>
  <div class="service-row reverse">
    <div class="service-photo" role="img" aria-label="Close view of a worker operating automated production equipment" style="background:linear-gradient(135deg,#1f3550,#5f86a8)"></div>
    <div class="service-text"><h3>Manufacturing Performance</h3><p>Lorem ipsum dolor sit amet, consectetur adipiscing elit. Nulla sed cum nunc, egestas placerat vulputate id vitae, a id pellentesque suspendisse tortor mi elementum interdum mauris venenatis lorem ipsum dolor sit amet, consectetur adipiscing elit. Nulla sed cum nunc, egestas placerat vulputate id vitae, a id pellentesq.</p></div>
  </div>
  <div class="service-row">
    <div class="service-photo" role="img" aria-label="Engineer in hard hat and ear defenders working on plant equipment" style="background:linear-gradient(135deg,#e8e2d8,#6f8a74)"></div>
    <div class="service-text"><h3>Major Equipment</h3><p>Lorem ipsum dolor sit amet, consectetur adipiscing elit. Nulla sed cum nunc, egestas placerat vulputate id vitae, a id pellentesque suspendisse tortor mi elementum interdum mauris venenatis lorem ipsum dolor sit amet, consectetur adipiscing elit. Nulla sed cum nunc, egestas placerat vulputate id vitae, a id pellentesq.</p></div>
  </div>
  <div class="service-row reverse">
    <div class="service-photo" role="img" aria-label="Technician in blue cleanroom suit commissioning a production line" style="background:linear-gradient(135deg,#dfe6ec,#7fa2bf)"></div>
    <div class="service-text"><h3>Commissioning</h3><p>Lorem ipsum dolor sit amet, consectetur adipiscing elit. Nulla sed cum nunc, egestas placerat vulputate id vitae, a id pellentesque suspendisse tortor mi elementum interdum mauris venenatis lorem ipsum dolor sit amet, consectetur adipiscing elit. Nulla sed cum nunc, egestas placerat vulputate id vitae, a id pellentesq.</p></div>
  </div>
</section>

<section class="reviews">
  <h2 class="section-title">REVIEWS</h2>
  <div class="review-cards">
    <div class="review-card">
      <div class="review-top"><div class="quote">&ldquo;</div><p>Their team kept our line running and cut downtime fast. Clear planning, honest advice and real results on the factory floor.</p></div>
      <div class="avatar" role="img" aria-label="Reviewer portrait"></div>
      <div class="review-name">LIAM HARTLEY</div>
      <div class="review-social"><span></span><span></span><span></span></div>
    </div>
    <div class="review-card">
      <div class="review-top"><div class="quote">&ldquo;</div><p>A reliable partner for maintenance design. Every project was delivered on time and our engineers learned a lot.</p></div>
      <div class="avatar" role="img" aria-label="Reviewer portrait"></div>
      <div class="review-name">LIAM HARTLEY</div>
      <div class="review-social"><span></span><span></span><span></span></div>
    </div>
    <div class="review-card">
      <div class="review-top"><div class="quote">&ldquo;</div><p>Practical, quick and easy to work with. The fit-out of our new plant went smoother than we ever expected.</p></div>
      <div class="avatar" role="img" aria-label="Reviewer portrait"></div>
      <div class="review-name">LIAM HARTLEY</div>
      <div class="review-social"><span></span><span></span><span></span></div>
    </div>
  </div>
</section>

<section class="contact">
  <div class="contact-box">
    <div class="contact-photo" role="img" aria-label="Two support staff with headsets working at a laptop"></div>
    <div class="contact-form">
      <h2>CONTACT US</h2>
      <span class="field">Your Name</span>
      <span class="field">Email Address</span>
      <span class="field">Phone number</span>
      <span class="field message">Message</span>
      <a class="btn" href="#" style="padding:8px 44px">Submit</a>
    </div>
    <svg class="contact-corner" width="70" height="55" viewBox="0 0 70 55" aria-hidden="true"><path d="M70 0 V55 H0 Z" fill="#0aa2df"/></svg>
  </div>
</section>

<footer class="site-footer">
  <svg class="footer-curve" width="1200" height="130" viewBox="0 0 1200 130" aria-hidden="true">
    <path d="M0 0 H1200 V10 C1150 90 1050 95 900 100 L0 110 Z" fill="#ffffff"/>
  </svg>
  <div class="footer-inner">
    <div class="footer-about">
      <div class="footer-brand"><span class="brand-mark"></span>Corrick &amp; Associates</div>
      <p>Corrick is a full service engineering consulting firm that helps manufacturers plan, build and run better plants. With Trivolt Engineering, our maintenance and reliability partner, we deliver lasting improvements and long-term value for every client.</p>
    </div>
    <div class="footer-col col-quick"><h4>QUICK LINKS</h4><ul><li>Home</li><li>About us</li><li>Services</li><li>Contact</li></ul></div>
    <div class="footer-col col-services"><h4>SERVICES</h4><ul><li>Process &amp; Facilities Design</li><li>Project Management</li><li>Major Equipment and Services</li><li>Contact</li><li>Engineering &amp; Maintenance Management</li><li>Maintenance Execution</li><li>Manufacturing Performance Measurement</li><li>SCADA</li></ul></div>
    <div class="footer-col"><h4>SOCIAL LINKS</h4>
      <div class="email-box">email<svg width="10" height="10" viewBox="0 0 10 10"><path d="M0 5 L10 0 L7 10 L5 6 Z" fill="none" stroke="#333" stroke-width="1"/></svg></div>
      <div class="footer-social"><span></span><span></span><span></span><span></span></div>
    </div>
  </div>
  <div class="copyright">© 2020 corrick associates, llc. all rights reserved</div>
</footer>

</div>
</body>
</html>
```